" Somos uma empresa especialista no ramos da engenharia elétrica no que tange a quadros elétricos. Atendemos empresas de engenharia, construção civil, industria, comercio, empreiteiras, engenheiros e técnicos eletricistas, além de revendas de materiais eletricos. Recebemos consultas através da nossa HOME PAGE, E MAIL , TELEFONE e PRESENCIAL. Somos especialistas em materiais específicos para aplicação em toda gama de quadros elétricos e automação e monitoramento de sistemas de energia elétrica. Recebemos o Projeto do cliente e executamos a montagem dos quadros. "

```html
<!DOCTYPE html>
<html lang="pt-BR">
<head>
<meta charset="utf-8">
<title>Lemos Prado — Quadros Elétricos</title>
<link rel="stylesheet" href="https://fonts.googleapis.com/css2?family=Roboto+Condensed:wght@400;700&family=Titillium+Web:wght@600;700&family=Roboto:wght@400;500&display=swap">
<style>
  :root{
    --navy:#25242e;
    --navy-deep:#1b1a22;
    --yellow:#f5c21b;
    --white:#ffffff;
    --muted:#c9c7cf;
    --brick-dark:#2a1d18;
    --brick-mid:#4a3026;
  }
  *{box-sizing:border-box;margin:0;padding:0}
  html,body{width:1200px;height:1200px;overflow:hidden;background:var(--navy-deep)}
  body{position:relative;font-family:"Roboto",Arial,sans-serif;color:var(--white)}

  /* Header */
  .site-header{position:absolute;left:0;top:0;width:1200px;height:125px;background:var(--navy)}
  .nav{position:absolute;top:32px;display:flex;gap:12px;font-family:"Roboto Condensed",Arial Narrow,sans-serif;font-size:18px;text-transform:uppercase;white-space:nowrap}
  .nav a{color:var(--white);text-decoration:none}
  .nav a.is-active{color:var(--yellow)}
  .nav--left{right:722px}
  .nav--right{left:730px}
  .brand{position:absolute;left:500px;top:0;width:204px;height:125px;background:var(--white);display:flex;flex-direction:column;align-items:center;justify-content:center;gap:8px}
  .brand__mark{width:34px;height:34px;border-radius:50%;background:var(--yellow)}
  .brand__name{font-family:"Titillium Web",Arial,sans-serif;font-weight:600;font-size:21px;letter-spacing:2px;color:var(--navy);text-transform:uppercase}
  .brand__tag{font-size:9px;color:#8a8890;letter-spacing:.8px;text-transform:uppercase}
  .social{position:absolute;left:980px;top:34px;display:flex;gap:14px}
  .social span{width:18px;height:18px;background:var(--yellow);border-radius:3px}
  .contact-bar{position:absolute;left:735px;top:90px;display:flex;gap:16px;white-space:nowrap}
  .contact-item{display:flex;gap:6px;align-items:flex-start}
  .contact-item svg{flex:none}
  .contact-item b{display:block;font-size:10px;font-weight:500}
  .contact-item small{display:block;font-size:8.5px;color:var(--muted)}
  .header-tools{position:absolute;left:1128px;top:94px;display:flex;gap:14px}

  /* Hero */
  .hero{position:absolute;left:0;top:125px;width:1200px;height:435px;background:linear-gradient(90deg,#5b5d63 0%,#8b8e94 30%,#b5b8bd 55%,#9a9da3 80%,#6f7278 100%)}
  .hero__photo{position:absolute;inset:0}
  .hero__arrow{position:absolute;top:130px}
  .hero__arrow--prev{left:0}
  .hero__arrow--next{right:0}
  .hero__title{position:absolute;left:80px;top:218px;height:58px;padding:0 22px;background:var(--yellow);color:var(--navy);font-family:"Titillium Web",Arial,sans-serif;font-weight:700;font-size:33px;line-height:58px;white-space:nowrap}
  .hero__cta{position:absolute;left:80px;top:298px;height:48px;width:165px;padding-left:18px;background:rgba(37,36,46,.85);font-family:"Titillium Web",Arial,sans-serif;font-weight:600;font-size:20px;line-height:48px;color:var(--white);display:flex;gap:24px;align-items:center}

  /* Feature cards */
  .features{position:absolute;left:150px;top:510px;width:900px;height:140px;display:flex}
  .feature{flex:1;background:var(--navy);display:flex;gap:16px;padding:22px 18px;border-right:1px solid #3a3945}
  .feature:last-child{border-right:0}
  .feature__icon{flex:none;margin-top:6px}
  .feature h3{font-family:"Titillium Web",Arial,sans-serif;font-weight:700;font-size:17px;line-height:19px;color:var(--yellow);text-transform:uppercase;margin-bottom:6px}
  .feature p{font-size:12px;line-height:15px;color:var(--muted)}

  /* Products */
  .wall{position:absolute;left:0;top:560px;width:1200px;height:640px;background:radial-gradient(ellipse at 50% 20%,var(--brick-mid) 0%,var(--brick-dark) 65%,#150f0c 100%)}
  .wall__glow{position:absolute;left:380px;top:620px;width:440px;height:120px;background:radial-gradient(ellipse at center,rgba(255,220,150,.25),rgba(255,220,150,0) 70%)}
  .section-title{position:absolute;left:0;top:685px;width:1200px;text-align:center;font-family:"Titillium Web",Arial,sans-serif;font-weight:700;font-size:40px;color:var(--white)}
  .section-title span{color:var(--yellow)}
  .products{position:absolute;left:90px;top:765px;width:1020px;height:345px;border:14px solid var(--yellow);background:var(--white)}
  .product{position:absolute;overflow:hidden;background:var(--white)}
  .product__photo{position:absolute;inset:0;background:linear-gradient(135deg,#d3d5d8,#a9acb1 60%,#c7c9cc)}
  .product__label{position:absolute;height:26px;background:var(--navy);color:var(--yellow);font-family:"Roboto Condensed",Arial Narrow,sans-serif;font-weight:700;font-size:17px;line-height:26px;text-align:center;text-transform:uppercase}
  .p1{left:0;top:0;width:375px;height:158px}
  .p2{left:375px;top:0;width:330px;height:158px}
  .p3{left:0;top:158px;width:375px;height:159px}
  .p4{left:375px;top:158px;width:330px;height:159px}
  .p5{left:705px;top:0;width:287px;height:317px}
  .p1 .product__label{left:40px;right:0;bottom:0}
  .p2 .product__label{left:0;right:30px;bottom:0}
  .p3 .product__label{left:40px;right:0;bottom:0}
  .p4 .product__label{left:0;right:60px;bottom:0}
  .p5 .product__label{left:0;right:0;top:0}
  .p5 .product__photo{top:26px;background:linear-gradient(135deg,#f0f0f1,#cfd1d4 55%,#e3e4e6)}
  .dots{position:absolute;left:0;top:1118px;width:1200px;display:flex;justify-content:center;gap:8px}
  .dots span{width:8px;height:8px;border-radius:50%;background:var(--white);opacity:.6}
  .dots span.is-active{opacity:1}
</style>
</head>
<body>

<header class="site-header">
  <nav class="nav nav--left">
    <a class="is-active">Home</a><a>Empresas</a><a>Produtos</a>
  </nav>
  <div class="brand">
    <span class="brand__mark"></span>
    <span class="brand__name">Lemos Prado</span>
    <span class="brand__tag">montagem de quadros elétricos</span>
  </div>
  <nav class="nav nav--right">
    <a>Serviços</a><a>Cases</a><a>Contato</a>
  </nav>
  <div class="social" aria-label="Redes sociais"><span></span><span></span><span></span><span></span></div>
  <div class="contact-bar">
    <div class="contact-item">
      <svg width="14" height="14" viewBox="0 0 16 16"><path d="M3 1h3l1 4-2 1a9 9 0 0 0 5 5l1-2 4 1v3a2 2 0 0 1-2 2A13 13 0 0 1 1 3a2 2 0 0 1 2-2z" fill="#f5c21b"/></svg>
      <div><b>Suporte</b><small>(11) 4000-1234</small></div>
    </div>
    <div class="contact-item">
      <svg width="14" height="14" viewBox="0 0 16 16"><circle cx="8" cy="8" r="7" fill="none" stroke="#f5c21b" stroke-width="2"/><path d="M8 4v4l3 2" stroke="#f5c21b" stroke-width="2" fill="none"/></svg>
      <div><b>Horário</b><small>Seg a Sex 8h às 18h</small></div>
    </div>
    <div class="contact-item">
      <svg width="14" height="14" viewBox="0 0 16 16"><rect x="1" y="3" width="14" height="10" fill="none" stroke="#f5c21b" stroke-width="2"/><path d="M1 3l7 6 7-6" fill="none" stroke="#f5c21b" stroke-width="2"/></svg>
      <div><b>E-mail</b><small>contato@lemosprado.com.br</small></div>
    </div>
  </div>
  <div class="header-tools">
    <svg width="16" height="16" viewBox="0 0 18 18"><circle cx="7.5" cy="7.5" r="5.5" fill="none" stroke="#fff" stroke-width="2"/><path d="M12 12l5 5" stroke="#fff" stroke-width="2"/></svg>
    <svg width="16" height="16" viewBox="0 0 18 18"><path d="M1 3h16M1 9h16M1 15h16" stroke="#fff" stroke-width="2"/></svg>
  </div>
</header>

<section class="hero">
  <div class="hero__photo" role="img" aria-label="Foto de quadro elétrico aberto com disjuntores e fiação"></div>
  <svg class="hero__arrow hero__arrow--prev" width="40" height="40" viewBox="0 0 40 40"><path d="M20 6L8 20l12 14M32 6L20 20l12 14" fill="none" stroke="#fff" stroke-width="4"/></svg>
  <svg class="hero__arrow hero__arrow--next" width="40" height="40" viewBox="0 0 40 40"><path d="M20 6l12 14-12 14M8 6l12 14L8 34" fill="none" stroke="#fff" stroke-width="4"/></svg>
  <h1 class="hero__title">Especialistas em automação e quadros elétricos</h1>
  <a class="hero__cta">Saiba mais <svg width="12" height="18" viewBox="0 0 12 18"><path d="M2 2l8 7-8 7" fill="none" stroke="#f5c21b" stroke-width="3"/></svg></a>
</section>

<div class="wall" role="img" aria-label="Fundo de parede de tijolos escuros iluminada"></div>
<div class="wall__glow"></div>

<section class="features">
  <article class="feature">
    <svg class="feature__icon" width="34" height="40" viewBox="0 0 34 40"><rect x="2" y="2" width="30" height="36" fill="none" stroke="#f5c21b" stroke-width="2"/><path d="M19 8l-6 12h6l-4 12" fill="none" stroke="#f5c21b" stroke-width="2"/></svg>
    <div><h3>Painéis<br>gerais</h3><p>Painéis desenvolvidos e projetados de acordo com as necessidades dos seus clientes</p></div>
  </article>
  <article class="feature">
    <svg class="feature__icon" width="44" height="30" viewBox="0 0 44 30"><rect x="1" y="1" width="42" height="28" fill="none" stroke="#f5c21b" stroke-width="2"/><path d="M7 8v14M13 8v14M19 8v14M25 8v14M31 8v14M37 8v14" stroke="#f5c21b" stroke-width="3"/></svg>
    <div><h3>Controle e<br>automação</h3><p>Totalmente modulares, permitindo o controle completamente centralizado.</p></div>
  </article>
  <article class="feature">
    <svg class="feature__icon" width="30" height="40" viewBox="0 0 30 40"><rect x="2" y="2" width="26" height="36" fill="none" stroke="#f5c21b" stroke-width="2"/><path d="M22 18v4" stroke="#f5c21b" stroke-width="2"/></svg>
    <div><h3>Caixas e<br>painéis</h3><p>Caixas e painéis vazios, para montadora de painéis, fabricantes de máquinas e outras empresas em geral.</p></div>
  </article>
</section>

<h2 class="section-title">Nossos <span>Produtos</span></h2>

<section class="products">
  <div class="product p1"><div class="product__photo" role="img" aria-label="Foto de painéis elétricos gerais"></div><div class="product__label">Painéis gerais</div></div>
  <div class="product p2"><div class="product__photo" role="img" aria-label="Foto de painéis especiais em aço inox"></div><div class="product__label">Painéis especiais</div></div>
  <div class="product p3"><div class="product__photo" role="img" aria-label="Foto de painéis de controle e automação"></div><div class="product__label">Controle e automação</div></div>
  <div class="product p4"><div class="product__photo" role="img" aria-label="Foto de caixas metálicas para painéis"></div><div class="product__label">Painéis de caixa</div></div>
  <div class="product p5"><div class="product__label">Quadros de distribuição</div><div class="product__photo" role="img" aria-label="Foto de quadros de distribuição com disjuntores"></div></div>
</section>

<div class="dots"><span class="is-active"></span><span></span><span></span><span></span><span></span></div>

</body>
</html>
```